New design for Crewnook

We are at the start of the process of evolving an existing business, and have just developed a new logo that will guide the look and feel of the rest of the site.

PeopleDesk.com.au will be the place to go for small business owners that need guidance and tools on how to look after HR functions such as recruitment and performance management amongst other aspects.

The existing site that is going to be evolved in www.hiringcornerfolk.com.au - while some of the content will remain, the entire look of the site needs to change, and a new homepage and other pages need to be developed.

For this project, we'd like the new homepage to be designed to lead the way for how the rest of the pages will look moving forward.

We're looking for a clean, clear and modern design. It should not feel cluttered or busy

The wireframe for the new homepage, and another landing page are attached.

Target Market(s)

Small and medium business owners - slightly male skew

Industry/Entity Type

Small Business

Requirements
Must have
• - Should be clean and simple
- The overall feel from the new logo (attached to the project) should be integrated into all elements of the site
- Should communicate that the site is easy to navigate
- Should communicate that the site is friendly and approachable
- Should communicate that the site is professional (for small businesses)
Nice to have
• This homepage for this site is quite a good design reference in terms of clean design.

http://www.choremoose.com/

For Crewnook though, the 3 boxes under the main image should appear above the fold though.

Also, happy for one other colour to be introduced to highlight call to action buttons etc.
Should not have
• Must not be cluttered
Should not introduce more than one additional colour to the existing colours from the logo

```html
<!DOCTYPE html>
<html lang="en">
<head>
<meta charset="utf-8">
<title>Crewnook – Recruitment and Performance Management</title>
<link href="https://fonts.googleapis.com/css2?family=Arimo:wght@400;700&family=Roboto+Condensed:wght@400;700&family=Noto+Serif:wght@700&display=swap" rel="stylesheet">
<style>
:root{
  --brand-blue:#1a6fb8;
  --brand-blue-dark:#0d4f8a;
  --nav-dark:#3b3b3b;
  --nav-darker:#2a2a2a;
  --page-bg:#ececec;
  --panel:#ffffff;
  --card-bg:#f3f3f3;
  --text:#333333;
  --text-soft:#7a7a7a;
  --line:#d6d6d6;
  --footer:#6d6d6d;
}
*{box-sizing:border-box;margin:0;padding:0}
html,body{width:1081px;height:1200px;overflow:hidden;background:var(--page-bg)}
body{font-family:"Arimo",Arial,sans-serif;color:var(--text)}
.stage{position:relative;width:1000px;height:1110px;transform:scale(1.081);transform-origin:0 0;background:var(--page-bg)}
.abs{position:absolute}

.top-rule{left:0;top:0;width:1000px;height:4px;background:var(--brand-blue)}
.site-header{left:0;top:4px;width:1000px;height:100px;background:#fff;border-bottom:1px solid #dcdcdc;box-shadow:0 2px 3px rgba(0,0,0,.05)}
.brand{left:16px;top:28px;display:flex;align-items:center;gap:8px}
.brand-dot{width:34px;height:34px;border-radius:50%;background:var(--brand-blue)}
.brand-name{font-family:"Roboto Condensed",sans-serif;font-weight:700;font-size:27px;color:var(--brand-blue);letter-spacing:-.3px}

.main-nav{left:222px;top:30px;width:768px;height:50px;background:linear-gradient(#474747,var(--nav-darker));border-radius:3px;box-shadow:0 8px 10px -6px rgba(0,0,0,.35);display:flex;align-items:center;padding:0 4px 0 15px}
.main-nav::before{content:"";position:absolute;left:6px;right:6px;top:4px;bottom:4px;border-top:1px dashed #777;border-bottom:1px dashed #777;pointer-events:none}
.nav-item{position:relative;flex:1 1 auto;justify-content:center;white-space:nowrap;font-family:"Roboto Condensed",sans-serif;font-weight:700;font-size:14.5px;color:#fff;height:50px;display:flex;align-items:center;padding:0 8px;border-right:1px solid #555}
.nav-item:last-child{border-right:0}
.nav-item.is-active{flex:0 0 auto;background:var(--brand-blue);height:52px;margin-top:-4px;border-radius:2px;padding:0 7px;margin-right:8px;border-right:0}

.social{left:12px;top:126px;display:flex;gap:14px}
.social span{width:16px;height:16px;border-radius:50%;background:#8a8a8a}
.social span:first-child{background:var(--brand-blue)}
.phone{right:5px;top:121px;font-family:"Noto Serif",serif;font-weight:700;font-size:20px;letter-spacing:1px;color:#111}

.panel{left:4px;top:163px;width:992px;height:827px;background:var(--panel);border:1px solid var(--line)}
.hero{left:12px;top:170px;width:976px;height:315px;background:linear-gradient(100deg,#3a3d42 0%,#4f5458 36%,#b9c0c6 45%,#8d8a86 62%,#cfd8e0 80%,#e6ecf0 100%)}
.hero-title{left:90px;top:290px;color:#fff;font-family:"Arimo",sans-serif;font-weight:700;text-shadow:0 2px 3px rgba(0,0,0,.6);letter-spacing:1px}
.hero-title .l1{font-size:28px;display:block}
.hero-title .l1 small{font-size:24px}
.hero-title .l2{font-size:20px;display:block;margin-top:14px}
.hero-title .l2 b{font-size:21px}

.about-title{left:19px;top:509px;font-family:"Roboto Condensed",sans-serif;font-weight:700;font-size:18px;color:#2e2e2e}
.about-text{left:19px;top:543px;width:962px;font-size:12.4px;line-height:18px;color:var(--text-soft)}
.about-text a{color:var(--brand-blue);text-decoration:none}
.divider{left:15px;top:630px;width:970px;height:12px}

.card{top:667px;width:298px;height:298px;background:var(--card-bg);border:1px solid #c9c9c9}
.card-photo{position:absolute;left:1px;top:1px;width:294px;height:147px}
.card-text{position:absolute;left:8px;top:157px;width:282px;font-size:11px;line-height:18px;color:#333}
.card-bar{position:absolute;left:0;bottom:0;width:296px;height:25px;background:linear-gradient(var(--brand-blue),var(--brand-blue-dark));display:flex;align-items:center;justify-content:space-between;padding:0 8px}
.card-bar h3{font-family:"Roboto Condensed",sans-serif;font-weight:700;font-size:15px;color:#fff;letter-spacing:.3px}
.news-item{position:absolute;left:6px;width:286px;height:76px}
.news-thumb{position:absolute;left:0;top:0;width:92px;height:74px}
.news-copy{position:absolute;left:102px;top:2px;width:180px;font-size:11px;line-height:18px;color:#333}
.news-meta{display:flex;justify-content:space-between;width:170px;margin-top:0}
.news-meta time{color:var(--brand-blue-dark)}

.site-footer{left:0;top:1050px;width:1000px;height:60px;background:var(--footer)}
.footer-links{left:8px;top:1076px;font-family:"Roboto Condensed",sans-serif;font-weight:700;font-size:12px;color:#fff;word-spacing:2px}
.footer-brand{right:5px;top:1066px;width:120px;height:30px;background:#f4f4f4;border:1px solid #999;display:flex;align-items:center;justify-content:center;font-family:"Roboto Condensed",sans-serif;font-weight:700;font-size:18px;color:#555}
</style>
</head>
<body>
<div class="stage">
  <div class="abs top-rule"></div>
  <header class="abs site-header"></header>
  <div class="abs brand"><span class="brand-dot"></span><span class="brand-name">Crewnook</span></div>

  <nav class="abs main-nav">
    <span class="nav-item is-active">Attract</span>
    <span class="nav-item">Recruit</span>
    <span class="nav-item">Induction</span>
    <span class="nav-item">Engage</span>
    <span class="nav-item">Performance Management</span>
    <span class="nav-item">Termination &amp; Redundancy</span>
    <span class="nav-item">Community</span>
  </nav>

  <div class="abs social" aria-label="Social links"><span></span><span></span><span></span><span></span></div>
  <div class="abs phone">+91 300 555 0142</div>

  <main class="abs panel"></main>
  <div class="abs hero" role="img" aria-label="Photo of business people in a recruitment interview"></div>
  <h1 class="abs hero-title"><span class="l1">RECRUITMENT <small>and</small></span><span class="l2">performance <b>MANAGEMENT</b></span></h1>

  <h2 class="abs about-title">ABOUT CREWNOOK</h2>
  <p class="abs about-text">Lorem Ipsum is simply dummy text of the printing and typesetting industry. Lorem Ipsum has been the industry's standard dummy text ever since the 1500s Lorem Ipsum is simply dummy text of the printing and typesetting industry. Lorem Ipsum has been the industry's standard dummy text ever since the 1500sLorem Ipsum is simply dummy text of the printing and typesetting industry. Lorem Ipsum has been the industry's standard dummy text ever since the 1500sLorem Ipsum is simply dummy text of the printing and typesetting industry. Lorem Ipsum has been the industry's standard dummy text ever since the 1500s <a href="#">MORE..</a></p>

  <svg class="abs divider" viewBox="0 0 970 12" aria-hidden="true">
    <line x1="9" y1="6" x2="961" y2="6" stroke="#d8d8d8" stroke-width="1.5"/>
    <circle cx="5" cy="6" r="4.5" fill="#fff" stroke="#bbb"/>
    <circle cx="962" cy="6" r="4.5" fill="#fff" stroke="#bbb"/>
  </svg>

  <section class="abs card" style="left:31px">
    <div class="card-photo" role="img" aria-label="Photo of two colleagues shaking hands" style="background:linear-gradient(120deg,#3c3f44,#c9ced3 45%,#e9edf0 70%,#8a8f96)"></div>
    <p class="card-text">Lorem Ipsum is simply dummy text of the printing and typesetting industry. Lorem Ipsum has been the industry's standard dummy text ever since the 1500sLorem Ipsum is simply dummy text of the printing and typesetting industry. Lorem Ipsum has been the industry's standard dummy text ever since the 1500s</p>
    <div class="card-bar"><h3>PARTENS</h3><svg width="20" height="20" viewBox="0 0 20 20" aria-hidden="true"><circle cx="10" cy="10" r="9.5" fill="#e8e8e8"/><path d="M5.5 8l4.5 4.5L14.5 8" fill="none" stroke="#555" stroke-width="2.4"/></svg></div>
  </section>

  <section class="abs card" style="left:349px">
    <div class="card-photo" role="img" aria-label="Photo of a smiling team of office workers" style="background:linear-gradient(180deg,#f1f2f3,#b7bdc5 55%,#6f7d92)"></div>
    <p class="card-text">Lorem Ipsum is simply dummy text of the printing and typesetting industry. Lorem Ipsum has been the industry's standard dummy text ever since the 1500sLorem Ipsum is simply dummy text of the printing and typesetting industry. Lorem Ipsum has been the industry's standard dummy text ever since the 1500s</p>
    <div class="card-bar"><h3>COMMUNITY</h3><svg width="20" height="20" viewBox="0 0 20 20" aria-hidden="true"><circle cx="10" cy="10" r="9.5" fill="#e8e8e8"/><path d="M5.5 8l4.5 4.5L14.5 8" fill="none" stroke="#555" stroke-width="2.4"/></svg></div>
  </section>

  <section class="abs card" style="left:667px">
    <article class="news-item" style="top:9px">
      <div class="news-thumb" role="img" aria-label="Photo of colleagues at a laptop" style="background:linear-gradient(135deg,#3d4146,#c8cdd2)"></div>
      <div class="news-copy">Lorem Ipsum is simply dummy text of the printing and typesetting industry. Lorem Ipsum has been the<div class="news-meta"><span>By Tamsin</span><time>21st july.2012</time></div></div>
    </article>
    <article class="news-item" style="top:98px">
      <div class="news-thumb" role="img" aria-label="Photo of a pen on a printed chart" style="background:linear-gradient(135deg,#dfe9c9,#8fb35a 55%,#4d5a40)"></div>
      <div class="news-copy">Lorem Ipsum is simply dummy text of the printing and typesetting industry. Lorem Ipsum has been the<div class="news-meta"><span>By Tamsin</span><time>21st july.2012</time></div></div>
    </article>
    <article class="news-item" style="top:187px">
      <div class="news-thumb" role="img" aria-label="Photo of rolled newspapers" style="background:linear-gradient(135deg,#2f6fb0,#a7c7e6 55%,#e8eef4)"></div>
      <div class="news-copy">Lorem Ipsum is simply dummy text of the printing and typesetting industry. Lorem Ipsum has been the<div class="news-meta"><span>By Tamsin</span><time>21st july.2012</time></div></div>
    </article>
    <div class="card-bar"><h3>NEWS</h3><svg width="20" height="20" viewBox="0 0 20 20" aria-hidden="true"><circle cx="10" cy="10" r="9.5" fill="#e8e8e8"/><path d="M5.5 8l4.5 4.5L14.5 8" fill="none" stroke="#555" stroke-width="2.4"/></svg></div>
  </section>

  <footer class="abs site-footer"></footer>
  <div class="abs footer-links">© 2012 Privacy Policy &nbsp;|&nbsp; Terms &amp; Conditions &nbsp;|&nbsp; Sitemap &nbsp;|&nbsp; Contact</div>
  <div class="abs footer-brand">Crewnook</div>
</div>
</body>
</html>
```